Regionale Imkerei sucht Etiketten-Design
Sehr gutes Endergebnis. Hochprofessionelle Abwicklung. Hat jeden Änderungswunsch zügig umgesetzt. Sehr angenehme, zielorientierte Kommunikation. Wirklich zu empfehlen, gerne wieder!
Zielgruppe
Mein Vater und ich haben eine regionale Hobbyimkerei, die wir nach und nach ausbauen wollen. Seit 1949 imkert unsere Familie. Ich bin in dritter Generation eingestiegen und möchte neben meinem know-how den Verkauf und das Marketing voran treiben um mit der Imkerei einen Nebenerwerb zu schaffen. Unsere Zielgruppe sind bewusste Verbraucher/innen, die gerne regional, hochqualitativ und nachhaltig einkaufen. Die meisten Honiggläser verkaufen wir direkt an der Haustür. Bis jetzt sind nur zwei Läden beliefert. Das soll sich dank musterwerkstatt ändern.
Aufgabenstellung
Ich habe eine Ausschreibung im PDF Format verfasst und beigefügt.
Was dort fehlt sind die Lagerungshinweise: kühl, trocken und dunkel lagern.
Für weitere Rückfragen gerne melden.

```html
<!DOCTYPE html>
<html lang="de">
<head>
<meta charset="utf-8">
<title>Blütenhonig Etiketten</title>
<link href="https://fonts.googleapis.com/css2?family=Quicksand:wght@300;400&display=swap" rel="stylesheet">
<style>
  :root {
    --honey: #ebb50f;
    --meadow: #5ba72a;
    --ink: #333333;
    --paper: #ffffff;
    --shade: rgba(0, 0, 0, 0.32);
  }
  * { margin: 0; padding: 0; box-sizing: border-box; }
  html, body {
    width: 1200px;
    height: 1057px;
    overflow: hidden;
    background: var(--paper);
    font-family: "Quicksand", "Century Gothic", sans-serif;
    color: var(--ink);
  }
  .sheet { position: relative; width: 1200px; height: 1057px; }

  .label {
    position: absolute;
    left: 0;
    width: 1200px;
    height: 420px;
  }
  .label--honey { top: 0; --accent: var(--honey); }
  .label--meadow { top: 420px; --accent: var(--meadow); }

  .label__body {
    position: absolute;
    left: 85px;
    top: 134px;
    width: 1030px;
    height: 242px;
    background: var(--paper);
    box-shadow: 0 38px 38px -8px var(--shade);
  }
  .label__frames {
    position: absolute;
    left: 0;
    top: 0;
    width: 1200px;
    height: 420px;
  }
  .label__frames polyline {
    fill: none;
    stroke: var(--accent);
    stroke-width: 2;
    stroke-linejoin: miter;
  }

  .abs { position: absolute; white-space: nowrap; }

  .intro {
    left: 119px;
    top: 162px;
    width: 200px;
    text-align: center;
    font-size: 12.5px;
    line-height: 17px;
    font-weight: 400;
  }

  .title {
    right: 439px;
    top: 152px;
    font-size: 41px;
    font-weight: 300;
    color: var(--accent);
    letter-spacing: 0.5px;
  }
  .subtitle {
    right: 439px;
    top: 204px;
    font-size: 15px;
    font-weight: 400;
  }
  .brand {
    left: 492px;
    top: 268px;
    display: flex;
    align-items: center;
    gap: 8px;
    font-size: 17px;
    font-weight: 400;
  }
  .brand__dot {
    width: 12px;
    height: 12px;
    border-radius: 50%;
    background: var(--accent);
  }
  .web {
    right: 439px;
    top: 337px;
    font-size: 15px;
    font-weight: 400;
  }

  .producer {
    left: 875px;
    width: 200px;
    text-align: center;
  }
  .producer__address {
    top: 223px;
    font-size: 12.5px;
    line-height: 17px;
  }
  .producer__weight {
    top: 268px;
    font-size: 41px;
    font-weight: 300;
    color: var(--accent);
  }
  .producer__notes {
    top: 323px;
    font-size: 10.5px;
    line-height: 15px;
  }
</style>
</head>
<body>
<main class="sheet">

  <section class="label label--honey">
    <div class="label__body"></div>
    <svg class="label__frames" viewBox="0 0 1200 420" aria-hidden="true">
      <polyline points="145,124 115,140 115,265 222,326 330,265 330,140 301,124"/>
      <polyline points="887,373 868,362 868,238 975,176 1082,238 1082,362 1062,373"/>
    </svg>
    <p class="abs intro">Lorem ipsum dolor sit<br>amet, consectetuer<br>adipiscing elit, sed diam<br>nonummy nibh euismod<br>tincidunt ut laoreet dolore</p>
    <h1 class="abs title">BLÜTENHONIG</h1>
    <p class="abs subtitle">aus der Region</p>
    <div class="abs brand"><span class="brand__dot"></span>tannenfrost</div>
    <p class="abs web">www.tannenfrost.de</p>
    <p class="abs producer producer__address">Max Mustermann<br>Straße 123 . 1234 Ort</p>
    <p class="abs producer producer__weight">250g</p>
    <p class="abs producer producer__notes">mindestens haltbar bis:<br>Hergestellt in Deutschland.</p>
  </section>

  <section class="label label--meadow">
    <div class="label__body"></div>
    <svg class="label__frames" viewBox="0 0 1200 420" aria-hidden="true">
      <polyline points="145,124 115,140 115,265 222,326 330,265 330,140 301,124"/>
      <polyline points="887,373 868,362 868,238 975,176 1082,238 1082,362 1062,373"/>
    </svg>
    <p class="abs intro">Lorem ipsum dolor sit<br>amet, consectetuer<br>adipiscing elit, sed diam<br>nonummy nibh euismod<br>tincidunt ut laoreet dolore</p>
    <h2 class="abs title">BLÜTENHONIG</h2>
    <p class="abs subtitle">aus der Region</p>
    <div class="abs brand"><span class="brand__dot"></span>tannenfrost</div>
    <p class="abs web">www.tannenfrost.de</p>
    <p class="abs producer producer__address">Max Mustermann<br>Straße 123 . 1234 Ort</p>
    <p class="abs producer producer__weight">250g</p>
    <p class="abs producer producer__notes">mindestens haltbar bis:<br>Hergestellt in Deutschland.</p>
  </section>

</main>
</body>
</html>
```